i need a business card design for my family investment company "norvane holdings" based in dubai. its a diverse investment firm focusing on education, hospitality and automotive. the design has to be modern and try to incorporate the logo "E" in the design. details on card as follow

Tariq H Bin Rashoud
Managing Director
tariq@norvane.ae
www.norvane.ae

Harbor park,palmcrest tower, office 1730, dubai
tel. 04 3819025
mobile.050 4172958

Target Market(s)

card used for networking events and investor meetings

Industry/Entity Type

Hospitality

```html
<!DOCTYPE html>
<html lang="en">
<head>
<meta charset="utf-8">
<title>Norvane Holdings – Business Card</title>
<link rel="stylesheet" href="https://fonts.googleapis.com/css2?family=Lato:wght@300;400;700&display=swap">
<style>
  :root {
    --backdrop: #e9ebee;
    --card-white: #ffffff;
    --brand-blue: #44739b;
    --ink: #1c1c1c;
    --on-blue: #ffffff;
    --divider: rgba(255, 255, 255, 0.55);
  }
  * { box-sizing: border-box; margin: 0; padding: 0; }
  html, body {
    width: 1200px;
    height: 926px;
    overflow: hidden;
    background: var(--backdrop);
    font-family: "Lato", Arial, sans-serif;
  }
  .sheet {
    width: 1200px;
    height: 926px;
    display: flex;
    flex-direction: column;
    align-items: center;
    justify-content: center;
    gap: 44px;
  }
  .card {
    width: 640px;
    height: 366px;
    background: var(--card-white);
    box-shadow: 0 6px 18px rgba(0, 0, 0, 0.12);
    position: relative;
    overflow: hidden;
  }
  .wordmark {
    font-weight: 300;
    color: var(--ink);
    text-transform: uppercase;
    text-align: center;
    line-height: 1;
  }
  .wordmark__name {
    display: block;
    font-size: 58px;
    letter-spacing: 0.42em;
    padding-left: 0.42em;
  }
  .wordmark__sub {
    display: block;
    font-size: 15px;
    letter-spacing: 0.9em;
    padding-left: 0.9em;
    margin-top: 14px;
  }
  /* back side */
  .card--back {
    display: flex;
    align-items: center;
    justify-content: center;
  }
  /* front side */
  .card--front .card__top {
    height: 168px;
    display: flex;
    align-items: center;
    justify-content: center;
  }
  .card--front .wordmark__name { font-size: 50px; }
  .card--front .wordmark__sub { font-size: 13px; margin-top: 12px; }
  .card__band {
    position: absolute;
    left: 0; right: 0; bottom: 0;
    height: 198px;
    background: var(--brand-blue);
    color: var(--on-blue);
    text-align: center;
    padding-top: 20px;
  }
  .holder__name {
    font-size: 27px;
    font-weight: 300;
    letter-spacing: 0.01em;
  }
  .holder__name strong { font-weight: 700; }
  .holder__role {
    font-size: 17px;
    font-weight: 400;
    letter-spacing: 0.06em;
    margin-top: 2px;
  }
  .contacts {
    display: grid;
    grid-template-columns: 1fr auto 1fr;
    column-gap: 14px;
    row-gap: 2px;
    font-size: 15px;
    margin: 14px auto 0;
    width: 470px;
  }
  .contacts__item--left { text-align: right; }
  .contacts__item--right { text-align: left; }
  .contacts__label { font-weight: 700; }
  .contacts__rule { color: var(--divider); }
  .address {
    font-size: 18px;
    font-weight: 700;
    letter-spacing: 0.05em;
    text-transform: uppercase;
    margin-top: 14px;
  }
</style>
</head>
<body>
<main class="sheet">
  <section class="card card--back" aria-label="Card back">
    <div class="wordmark">
      <span class="wordmark__name">Norvane</span>
      <span class="wordmark__sub">Holdings</span>
    </div>
  </section>

  <section class="card card--front" aria-label="Card front">
    <div class="card__top">
      <div class="wordmark">
        <span class="wordmark__name">Norvane</span>
        <span class="wordmark__sub">Holdings</span>
      </div>
    </div>
    <div class="card__band">
      <h1 class="holder__name">Tariq <strong>H Bin Rashoud</strong></h1>
      <p class="holder__role">managing director</p>
      <div class="contacts">
        <span class="contacts__item--left"><span class="contacts__label">tel.</span> 04 3819025</span>
        <span class="contacts__rule">|</span>
        <span class="contacts__item--right"><span class="contacts__label">mobile.</span> 050 4172958</span>
        <span class="contacts__item--left"><span class="contacts__label">web.</span> www.norvane.ae</span>
        <span class="contacts__rule">|</span>
        <span class="contacts__item--right"><span class="contacts__label">email.</span> tariq@norvane.ae</span>
      </div>
      <p class="address">Harbor Park, Palmcrest Tower, Office 1730, Dubai</p>
    </div>
  </section>
</main>
</body>
</html>
```